Crumbly Corner needs a business card

Crumbly Corner needs an attractive, playful, and exciting business card design to attract potential buyers. I have included our logo, label, and social media design files along with the fonts and colors for ideas. For the logo file, please only pay attention to the purple background with white text. I want a card with premium matte and metallic finish. I want my name included, e-mail, and phone number. The logo must be included, and then use the label design and social media design files to add creativity to the design. Only the fonts that are provided should be used as well.

Name: Gregory Halvorsen
Phone: 555-274-8106
E-mail: ghalvorsen@crumblycornerco.example

Industry/Entity Type

Business

Contact Information for Business Card

I want a card with premium matte and metallic finish. I want my name included, e-mail, and phone number. The logo must be included, and then use the label design and social media design files to add creativity to the design. Only the fonts that are provided should be used as well.

Name: Gregory Halvorsen
Phone: 555-274-8106

Colors
6b449b

Requirements
Must have
• My logo, my fonts, my colors, my designs to some degree, and my character

```html
<!DOCTYPE html>
<html lang="en">
<head>
<meta charset="utf-8">
<title>Crumbly Corner – Business Card</title>
<link href="https://fonts.googleapis.com/css2?family=Roboto:wght@400;700&family=Kalam&display=swap" rel="stylesheet">
<style>
  :root {
    --purple: #371b5e;
    --white: #ffffff;
    --stage: #e9e8ec;
    --star-haze: #f1f0f4;
  }
  * { margin: 0; padding: 0; box-sizing: border-box; }
  html, body { width: 1200px; height: 960px; overflow: hidden; }
  body { background: var(--stage); font-family: "Roboto", sans-serif; position: relative; }

  .card {
    position: absolute;
    width: 600px;
    height: 342px;
    border-radius: 20px;
    overflow: hidden;
    background: var(--white);
  }
  .card--front { left: 314px; top: 113px; }
  .card--back  { left: 311px; top: 472px; }

  .front-wave { position: absolute; inset: 0; }

  .front-brand {
    position: absolute;
    left: 40px;
    top: 118px;
    width: 180px;
    color: var(--white);
    font-weight: 700;
    font-size: 30px;
    line-height: 1.1;
    text-align: center;
  }

  .contact {
    position: absolute;
    right: 34px;
    top: 204px;
    text-align: right;
    color: var(--purple);
  }
  .contact__name {
    font-weight: 700;
    font-size: 20px;
    letter-spacing: 0.2px;
    margin-bottom: 10px;
    white-space: nowrap;
  }
  .contact__line {
    display: flex;
    justify-content: flex-end;
    align-items: center;
    gap: 8px;
    font-size: 13px;
    line-height: 19px;
    white-space: nowrap;
  }
  .contact__icon { width: 12px; height: 12px; fill: var(--purple); flex: none; }

  .back-pattern {
    position: absolute;
    inset: 0;
    background: radial-gradient(circle at 50% 50%, var(--white) 0%, var(--star-haze) 100%);
  }
  .back-brand {
    position: absolute;
    left: 0; right: 0;
    top: 140px;
    text-align: center;
    color: var(--purple);
    font-weight: 700;
    font-size: 44px;
  }
  .back-site {
    position: absolute;
    left: 0; right: 0;
    top: 286px;
    text-align: center;
    color: var(--purple);
    font-family: "Kalam", cursive;
    font-size: 20px;
  }
</style>
</head>
<body>

  <section class="card card--front">
    <svg class="front-wave" viewBox="0 0 600 342" width="600" height="342" aria-hidden="true">
      <path d="M0 0 H572 C468 14 410 110 350 180 C290 250 200 318 20 342 H0 Z" fill="var(--purple)"/>
      <path d="M586 0 C482 18 424 120 364 192 C304 262 214 328 34 342" fill="none" stroke="var(--purple)" stroke-width="2"/>
    </svg>

    <div class="front-brand">Crumbly Corner</div>

    <div class="contact">
      <div class="contact__name">GREGORY HALVORSEN</div>
      <div class="contact__line">555-274-8106
        <svg class="contact__icon" viewBox="0 0 24 24"><path d="M6.6 10.8a15.1 15.1 0 0 0 6.6 6.6l2.2-2.2c.3-.3.7-.4 1-.2 1.1.4 2.3.6 3.6.6.6 0 1 .4 1 1V20c0 .6-.4 1-1 1A17 17 0 0 1 3 4c0-.6.4-1 1-1h3.5c.6 0 1 .4 1 1 0 1.3.2 2.5.6 3.6.1.3 0 .7-.2 1z"/></svg>
      </div>
      <div class="contact__line">ghalvorsen@crumblycornerco.example
        <svg class="contact__icon" viewBox="0 0 24 24"><path d="M2 5h20v14H2z" fill="var(--purple)"/><path d="M3 6l9 7 9-7" fill="none" stroke="#fff" stroke-width="1.6"/></svg>
      </div>
      <div class="contact__line">www.crumblycornerco.example
        <svg class="contact__icon" viewBox="0 0 24 24"><circle cx="12" cy="12" r="10"/><path d="M7 8c2 0 3 1 3 3s-2 2-2 4 M15 5c-1 2 1 3 2 4s-1 3 1 5" fill="none" stroke="#fff" stroke-width="1.6"/></svg>
      </div>
    </div>
  </section>

  <section class="card card--back">
    <div class="back-pattern" role="img" aria-label="Faint scattered sparkle star pattern"></div>
    <div class="back-brand">Crumbly Corner</div>
    <div class="back-site">www.crumblycornerco.example</div>
  </section>

</body>
</html>
```